Corvane Bookkeeping Services business cards

looking for a double sided business card design. My logo is attached. I am looking for a design similar to the attached. Keen to see what my logo in white on the blue background would look like.

```html
<!DOCTYPE html>
<html lang="en">
<head>
<meta charset="utf-8">
<title>Corvane Bookkeeping Services – Business Cards</title>
<link href="https://fonts.googleapis.com/css2?family=Montserrat:wght@500;600;700;800&display=swap" rel="stylesheet">
<style>
  :root {
    --backdrop: #d6d7d9;
    --navy: #1e3a6b;
    --green: #9bb53a;
    --white: #ffffff;
  }
  * { margin: 0; padding: 0; box-sizing: border-box; }
  html, body { width: 1200px; height: 1200px; overflow: hidden; }
  body {
    background: var(--backdrop);
    font-family: "Montserrat", Arial, sans-serif;
    position: relative;
  }
  .card {
    position: absolute;
    border-radius: 38px;
  }
  .card--front {
    left: 172px; top: 94px; width: 856px; height: 465px;
    background: var(--navy);
  }
  .card--back {
    left: 163px; top: 632px; width: 855px; height: 466px;
    background: var(--white);
  }
  .brand {
    position: absolute;
    display: flex;
    align-items: center;
    gap: 20px;
  }
  .brand__mark {
    width: 58px; height: 58px;
    background: var(--green);
    flex: none;
  }
  .brand__name {
    font-weight: 800;
    line-height: 1;
    letter-spacing: 0.5px;
  }
  .brand__name span { display: block; }
  .brand__name .brand__word { font-size: 70px; letter-spacing: -1px; }
  .brand__name .brand__line { font-size: 21px; margin-top: 6px; letter-spacing: 0.6px; text-transform: uppercase; }

  .card--front .brand { left: 160px; top: 140px; }
  .card--front .brand__name { color: var(--white); }
  .front__url {
    position: absolute; left: 0; right: 0; top: 304px;
    text-align: center;
    color: var(--white);
    font-size: 25px; font-weight: 600;
    letter-spacing: 11px;
  }

  .card--back .brand { left: 420px; top: 52px; }
  .card--back .brand__mark { width: 46px; height: 46px; }
  .card--back .brand__name { color: var(--navy); }
  .card--back .brand__name .brand__word { font-size: 56px; }
  .card--back .brand__name .brand__line { font-size: 17px; margin-top: 4px; }

  .accent-bar {
    position: absolute; width: 16px; background: var(--navy);
  }
  .accent-bar--left { left: 160px; top: 774px; height: 97px; }
  .accent-bar--right { left: 1002px; top: 950px; height: 88px; }

  .person { position: absolute; left: 232px; top: 786px; color: var(--navy); }
  .person__name { font-size: 29px; font-weight: 600; letter-spacing: 0.3px; }
  .person__role { font-size: 23px; font-weight: 500; margin-top: 10px; margin-left: 3px; }

  .contacts { position: absolute; left: 234px; top: 888px; list-style: none; color: var(--navy); }
  .contacts li {
    display: flex; align-items: center; gap: 12px;
    font-size: 23px; font-weight: 500; height: 42px;
  }
  .contacts svg { width: 20px; height: 20px; fill: var(--navy); flex: none; }

  .address {
    position: absolute; left: 664px; top: 968px;
    color: var(--navy); font-size: 23px; font-weight: 500; line-height: 40px;
    font-style: normal;
  }
</style>
</head>
<body>
  <section class="card card--front">
    <div class="brand">
      <div class="brand__mark"></div>
      <div class="brand__name">
        <span class="brand__word">Corvane</span>
        <span class="brand__line">Bookkeeping Services</span>
      </div>
    </div>
    <p class="front__url">www.yoursite.com</p>
  </section>

  <section class="card card--back">
    <div class="brand">
      <div class="brand__mark"></div>
      <div class="brand__name">
        <span class="brand__word">Corvane</span>
        <span class="brand__line">Bookkeeping Services</span>
      </div>
    </div>
  </section>

  <div class="accent-bar accent-bar--left"></div>
  <div class="accent-bar accent-bar--right"></div>

  <div class="person">
    <p class="person__name">YOUR NAME</p>
    <p class="person__role">Director</p>
  </div>

  <ul class="contacts">
    <li>
      <svg viewBox="0 0 20 20" aria-hidden="true"><path d="M2 7c0-3 3-4 8-4s8 1 8 4v1h-4V6.5c-1-.4-2.5-.5-4-.5s-3 .1-4 .5V8H2z"/><rect x="4" y="9" width="12" height="8" rx="2"/></svg>
      (123) 444-5555
    </li>
    <li>
      <svg viewBox="0 0 20 20" aria-hidden="true"><rect x="5" y="2" width="10" height="5"/><path d="M2 8h16v7h-3v-3H5v3H2z"/><rect x="6" y="13" width="8" height="5"/></svg>
      (123) 444-5556
    </li>
    <li>
      <svg viewBox="0 0 20 20" aria-hidden="true"><path d="M2 5h16v1l-8 5-8-5z"/><path d="M2 8l8 5 8-5v7H2z"/></svg>
      urmail@yoursite.com
    </li>
    <li>
      <svg viewBox="0 0 20 20" aria-hidden="true"><path fill-rule="evenodd" d="M10 2a8 8 0 1 1 0 16 8 8 0 0 1 0-16zm0 1.6c-1 1-1.7 2.9-1.9 5.4h3.8c-.2-2.5-.9-4.4-1.9-5.4zM3.7 9h2.9c.1-2 .5-3.7 1.2-5A6.4 6.4 0 0 0 3.7 9zm8.5-5c.7 1.3 1.1 3 1.2 5h2.9a6.4 6.4 0 0 0-4.1-5zM3.7 11a6.4 6.4 0 0 0 4.1 5c-.7-1.3-1.1-3-1.2-5zm4.4 0c.2 2.5.9 4.4 1.9 5.4 1-1 1.7-2.9 1.9-5.4zm5.3 0c-.1 2-.5 3.7-1.2 5a6.4 6.4 0 0 0 4.1-5z"/></svg>
      www.yoursite.com
    </li>
  </ul>

  <address class="address">
    1234 Your Address<br>
    Country Name, AA 1234
  </address>
</body>
</html>
```